Web Design for Financial Consulting Company

We need a website design for a financial consulting company "Korvane Consulting". We build financial models, scenario analysis, handle the budgeting process and provide temporary staffing. I have over 10 years of experience. My Excel expertise and analytical savvy has saved clients over $17 million in profit.

Target Market(s)

Small to medium businesses

Industry/Entity Type

Financial Consulting

Number of Pages Required

4 page

Requirements
Must have
• Professional looking
Nice to have
• A little futuristic looking

```html
<!DOCTYPE html>
<html lang="en">
<head>
<meta charset="utf-8">
<title>Korvane Consulting — Website Design</title>
<link href="https://fonts.googleapis.com/css2?family=Poppins:wght@400;500;600;700&display=swap" rel="stylesheet">
<style>
  :root{
    --blue:#18a6ee;
    --blue-light:#4cc0f7;
    --navy:#1b2734;
    --navy-deep:#141e29;
    --ink:#1a1f26;
    --muted:#4a5260;
    --line:#c9ced6;
    --white:#ffffff;
  }
  *{box-sizing:border-box;margin:0;padding:0}
  html,body{width:1200px;height:3714px;overflow:hidden;background:var(--white)}
  body{font-family:'Poppins',sans-serif;color:var(--ink);position:relative}
  .screen{position:absolute;left:0;width:1200px;overflow:hidden;background:var(--white)}
  .sidebar{position:absolute;left:0;top:0;width:60px;height:100%;background:var(--navy)}
  .menu-btn{position:absolute;left:0;top:0;width:60px;height:60px;background:var(--blue);display:flex;align-items:center;justify-content:center}
  .side-label{position:absolute;left:30px;color:var(--white);font-size:13px;transform:translate(-50%,0) rotate(-90deg);white-space:nowrap}
  .social{position:absolute;left:13px;width:34px;height:34px;border-radius:50%}
  .social.outline{border:1.5px solid var(--white)}
  .social.filled{background:var(--blue)}
  .topbar{position:absolute;left:60px;top:0;width:1140px;height:60px;background:var(--navy);z-index:3}
  .brand{position:absolute;left:22px;top:14px;display:flex;align-items:center;gap:10px;color:var(--white);font-weight:600;font-size:22px;letter-spacing:1px}
  .brand-mark{width:32px;height:32px;background:var(--blue)}
  .nav{position:absolute;left:0;top:0}
  .nav-item{position:absolute;top:0;height:60px;line-height:60px;color:var(--white);font-size:13px;text-align:center}
  .nav-item.active{background:var(--blue);height:68px}
  .cta{position:absolute;left:938px;top:10px;width:143px;height:40px;border:1.5px solid var(--blue);color:var(--white);font-size:13px;line-height:37px;padding-left:16px}
  .cta .arrow{position:absolute;right:0;top:0;width:38px;height:37px;background:var(--blue);display:flex;align-items:center;justify-content:center}
  .banner{position:absolute;left:60px;top:60px;width:840px;height:375px;background:linear-gradient(120deg,#3a4654 0%,#27333f 55%,#1f2a36 100%)}
  .banner-title{position:absolute;left:33px;bottom:50px;color:var(--white);font-size:37px;font-weight:600}
  .aside{position:absolute;left:900px;top:60px;width:300px;background:linear-gradient(160deg,#5cc8fa 0%,#31b1f2 50%,#1d9fe6 100%)}
  .aside-box{position:absolute;left:24px;color:var(--white)}
  .aside-box h3{font-size:26px;font-weight:600;line-height:1.2}
  .aside-box p{font-size:13px;line-height:20px;margin-top:4px;width:200px;opacity:.92}
  .btn{position:relative;display:inline-block;height:36px;background:var(--navy);color:var(--white);font-size:13px;line-height:36px;padding:0 54px 0 16px;border:1px solid var(--white)}
  .btn .arrow{position:absolute;right:-1px;top:-1px;width:40px;height:36px;background:var(--blue);display:flex;align-items:center;justify-content:center}
  .footer{position:absolute;left:0;width:1200px;height:37px;background:var(--navy);color:var(--white);font-size:12px;text-align:center;line-height:37px}
  .accent{color:var(--blue)}

  /* Home */
  .hero{position:absolute;left:60px;top:60px;width:1140px;height:598px;background:linear-gradient(100deg,#2c3946 0%,#3e4c59 45%,#56636f 70%,#3a4a5a 100%)}
  .hero-rule{position:absolute;left:60px;top:657px;width:1140px;height:3px;background:var(--blue)}
  .hero h1{position:absolute;left:44px;top:255px;color:var(--white);font-size:46px;font-weight:600;line-height:56px}
  .hero p{position:absolute;left:44px;top:380px;width:570px;color:var(--white);font-size:13px;line-height:20px}
  .hero .btn{position:absolute;left:42px;top:447px}

  /* About */
  .about-frame{position:absolute;left:90px;top:488px;width:340px;height:306px;background:var(--blue)}
  .about-photo{position:absolute;left:23px;top:22px;width:275px;height:280px;background:linear-gradient(135deg,#eef2f6 0%,#c9d6e2 60%,#8ea3b8 100%)}
  .about-copy{position:absolute;left:475px;top:522px;width:390px}
  .about-copy h2{font-size:38px;font-weight:600;line-height:46px}
  .about-copy p{margin-top:12px;font-size:13px;line-height:22.5px;color:var(--muted)}

  /* Services */
  .section-title{position:absolute;left:60px;width:840px;text-align:center;font-size:30px;font-weight:600}
  .card{position:absolute;width:252px;height:211px;background:var(--white);box-shadow:0 0 10px rgba(20,30,40,.13);text-align:center;padding:16px 18px 0}
  .card.featured{background:var(--navy);color:var(--white)}
  .card h4{font-size:16px;font-weight:600;line-height:26px;margin-top:8px}
  .card.featured h4{color:var(--blue)}
  .card p{font-size:13px;line-height:22.5px;color:var(--muted);margin-top:4px}
  .card.featured p{color:var(--white)}
  .card svg{display:block;margin:0 auto}

  /* Contact */
  .form-title{position:absolute;left:93px;font-size:28px;font-weight:600}
  .field{position:absolute;height:36px;border:1px solid #8a929c;font-size:12px;line-height:34px;padding-left:16px;color:#3a3f46}
  .field.focus{border-color:#7cc9f2}
  .field .caret{position:absolute;right:26px;top:14px}
  .map{position:absolute;left:91px;width:769px;height:261px;background:linear-gradient(135deg,#f3f5f7 0%,#e6eaee 100%)}
</style>
</head>
<body>

<!-- HOME -->
<section class="screen" style="top:0;height:660px">
  <div class="hero" role="img" aria-label="Consultant working beside a monitor showing charts, with a blue bar-chart graphic">
    <h1>Helping your <span class="accent">finance team</span><br><span class="accent">and increasing profit</span></h1>
    <p>Lorem Ipsum is simply dummy text of the printing and typesetting industry. Lorem Ipsum has been the industry's standard dummy text.</p>
    <span class="btn">Contact Us Today<span class="arrow"><svg width="16" height="14" viewBox="0 0 16 14"><path d="M1 7h13M8 1l6 6-6 6" stroke="#fff" stroke-width="2" fill="none"/></svg></span></span>
  </div>
  <div class="hero-rule"></div>
  <div class="sidebar">
    <div class="menu-btn"><svg width="18" height="14" viewBox="0 0 18 14"><path d="M0 1h18M0 7h12M0 13h16" stroke="#fff" stroke-width="2"/></svg></div>
    <div class="side-label" style="top:130px">Home</div>
    <div class="social outline" style="top:537px"></div>
    <div class="social filled" style="top:583px"></div>
  </div>
  <div class="topbar">
    <div class="brand"><span class="brand-mark"></span>Korvane Consulting</div>
    <div class="nav">
      <div class="nav-item active" style="left:542px;width:60px">Home</div>
      <div class="nav-item" style="left:630px;width:50px">About</div>
      <div class="nav-item" style="left:718px;width:64px">Services</div>
      <div class="nav-item" style="left:822px;width:80px">Contact Us</div>
    </div>
    <div class="cta">Get Started<span class="arrow"><svg width="16" height="14" viewBox="0 0 16 14"><path d="M1 7h13M8 1l6 6-6 6" stroke="#fff" stroke-width="2" fill="none"/></svg></span></div>
  </div>
</section>

<!-- ABOUT -->
<section class="screen" style="top:684px;height:888px">
  <div class="banner" role="img" aria-label="Stacked coins in front of a city skyline"><div class="banner-title">About Us</div></div>
  <div class="aside" style="height:792px" role="img" aria-label="Hands using a calculator and pen over financial papers">
    <div class="aside-box" style="top:578px">
      <h3>Contact Us</h3>
      <p>Lorem Ipsum is simply dummy text of the printing and typesetting industry.</p>
      <div style="margin-top:18px"><span class="btn">Contact Us<span class="arrow"><svg width="16" height="14" viewBox="0 0 16 14"><path d="M1 7h13M8 1l6 6-6 6" stroke="#fff" stroke-width="2" fill="none"/></svg></span></span></div>
    </div>
  </div>
  <div class="about-frame"><div class="about-photo" role="img" aria-label="Smiling consultant in a suit beside a monitor with charts"></div></div>
  <div class="about-copy">
    <h2>About <span class="accent">Korvane<br>Consulting</span></h2>
    <p>I am an experienced Finance professional who develops strategic financial plans, provides insightful analysis, and supports decision-making. With over 10 years of experience, I have successfully increased profitability for clients by $17M.</p>
  </div>
  <div class="footer" style="top:852px">© 2023 Copyright Korvane Consulting. All Right Reserved.</div>
  <div class="sidebar" style="height:852px">
    <div class="menu-btn"><svg width="18" height="14" viewBox="0 0 18 14"><path d="M0 1h18M0 7h12M0 13h16" stroke="#fff" stroke-width="2"/></svg></div>
    <div class="side-label" style="top:148px">About</div>
    <div class="social outline" style="top:787px"></div>
    <div class="social filled" style="top:833px;top:-100px"></div>
  </div>
  <div class="social filled" style="top:833px;left:13px;z-index:4"></div>
  <div class="topbar">
    <div class="brand"><span class="brand-mark"></span>Korvane Consulting</div>
    <div class="nav">
      <div class="nav-item" style="left:542px;width:60px">Home</div>
      <div class="nav-item active" style="left:627px;width:58px">About</div>
      <div class="nav-item" style="left:718px;width:64px">Services</div>
      <div class="nav-item" style="left:822px;width:80px">Contact Us</div>
    </div>
    <div class="cta">Get Started<span class="arrow"><svg width="16" height="14" viewBox="0 0 16 14"><path d="M1 7h13M8 1l6 6-6 6" stroke="#fff" stroke-width="2" fill="none"/></svg></span></div>
  </div>
</section>

<!-- SERVICES -->
<section class="screen" style="top:1595px;height:1024px">
  <div class="banner" role="img" aria-label="City skyline with a rising blue arrow"><div class="banner-title">Services</div></div>
  <div class="aside" style="height:927px" role="img" aria-label="Calculator and financial documents in blue tones">
    <div class="aside-box" style="top:718px">
      <h3>Contact Us</h3>
      <p>Lorem Ipsum is simply dummy text of the printing and typesetting industry.</p>
      <div style="margin-top:18px"><span class="btn">Contact Us<span class="arrow"><svg width="16" height="14" viewBox="0 0 16 14"><path d="M1 7h13M8 1l6 6-6 6" stroke="#fff" stroke-width="2" fill="none"/></svg></span></span></div>
    </div>
  </div>
  <div class="section-title" style="top:458px">Our <span class="accent">Services</span></div>

  <div class="card" style="left:88px;top:518px">
    <svg width="44" height="48" viewBox="0 0 44 48" fill="none" stroke="#1a1f26" stroke-width="1.6"><rect x="8" y="2" width="26" height="34"/><rect x="4" y="6" width="26" height="34" fill="#fff"/><path d="M9 14h10M9 19h14M9 34v-6M14 34v-9M19 34v-4M24 34v-11"/><rect x="26" y="30" width="14" height="16" fill="#fff"/><path d="M29 35h8M29 39h8M29 43h6"/></svg>
    <h4>Financial Models –<br>Projects</h4>
    <p>Financial analysis, scenario modeling, pricing analysis, projects</p>
  </div>
  <div class="card featured" style="left:355px;top:518px">
    <svg width="48" height="48" viewBox="0 0 48 48" fill="none" stroke="#18a6ee" stroke-width="1.6"><rect x="6" y="2" width="28" height="38"/><circle cx="20" cy="17" r="8"/><path d="M20 12v10M17 15h5a2 2 0 0 1 0 4h-4"/><path d="M11 31h18M11 35h12"/><rect x="28" y="28" width="16" height="18" fill="#1b2734"/><path d="M31 33h10M31 37h10M31 41h10M36 33v12"/></svg>
    <h4>Budgeting Process</h4>
    <p>Building budgets from scratch, revamping current process to be more robust and scalable.</p>
  </div>
  <div class="card" style="left:620px;top:518px">
    <svg width="50" height="48" viewBox="0 0 50 48" fill="none" stroke="#1a1f26" stroke-width="1.6"><circle cx="25" cy="10" r="6"/><path d="M15 24c0-5 4-8 10-8s10 3 10 8"/><circle cx="25" cy="31" r="6"/><circle cx="25" cy="31" r="2"/><path d="M25 23v2M25 37v2M17 31h2M31 31h2"/><circle cx="8" cy="36" r="4"/><path d="M2 46c0-4 3-6 6-6s6 2 6 6"/><circle cx="42" cy="36" r="4"/><path d="M36 46c0-4 3-6 6-6s6 2 6 6"/></svg>
    <h4>Temporary Staffing</h4>
    <p>Years of Financial Planning and Analysis experience across multiple industries can help temporary staffing needs.</p>
  </div>
  <div class="card" style="left:189px;top:742px">
    <svg width="48" height="50" viewBox="0 0 48 50" fill="none" stroke="#1a1f26" stroke-width="1.6"><path d="M6 2h22l8 8v34H6z"/><path d="M28 2v8h8"/><path d="M11 38v-6M16 38v-10M21 38v-7M26 38v-12"/><path d="M10 26l6-6 5 4 7-8"/><path d="M32 30l12 12-4 4-12-12z"/></svg>
    <h4>Data cleansing</h4>
  </div>
  <div class="card" style="left:455px;top:742px">
    <svg width="52" height="50" viewBox="0 0 52 50" fill="none" stroke="#1a1f26" stroke-width="1.6"><path d="M8 26V6M3 11l5-5 5 5M26 20V2M21 7l5-5 5 5M44 26V6M39 11l5-5 5 5"/><circle cx="14" cy="38" r="8"/><circle cx="14" cy="38" r="3"/><circle cx="34" cy="36" r="10"/><circle cx="34" cy="36" r="4"/></svg>
    <h4>Process Improvement</h4>
    <p>Month end close, reporting, budgeting</p>
  </div>

  <div class="footer" style="top:987px">© 2023 Copyright Korvane Consulting. All Right Reserved.</div>
  <div class="sidebar" style="height:987px">
    <div class="menu-btn"><svg width="18" height="14" viewBox="0 0 18 14"><path d="M0 1h18M0 7h12M0 13h16" stroke="#fff" stroke-width="2"/></svg></div>
    <div class="side-label" style="top:143px">Services</div>
    <div class="social outline" style="top:906px"></div>
    <div class="social filled" style="top:952px"></div>
  </div>
  <div class="topbar">
    <div class="brand"><span class="brand-mark"></span>Korvane Consulting</div>
    <div class="nav">
      <div class="nav-item" style="left:542px;width:60px">Home</div>
      <div class="nav-item" style="left:630px;width:50px">About</div>
      <div class="nav-item active" style="left:719px;width:66px">Services</div>
      <div class="nav-item" style="left:822px;width:80px">Contact Us</div>
    </div>
    <div class="cta">Get Started<span class="arrow"><svg width="16" height="14" viewBox="0 0 16 14"><path d="M1 7h13M8 1l6 6-6 6" stroke="#fff" stroke-width="2" fill="none"/></svg></span></div>
  </div>
</section>

<!-- CONTACT -->
<section class="screen" style="top:2637px;height:1077px">
  <div class="banner" role="img" aria-label="Business team discussing around a meeting table"><div class="banner-title">Contact Us</div></div>
  <div class="aside" style="height:981px" role="img" aria-label="Calculator and financial papers in blue tones">
    <div class="aside-box" style="top:781px">
      <h3>Our Services</h3>
      <p style="width:220px">Committed to providing you with a wide range of services.</p>
      <div style="margin-top:18px"><span class="btn">View All Services<span class="arrow"><svg width="16" height="14" viewBox="0 0 16 14"><path d="M1 7h13M8 1l6 6-6 6" stroke="#fff" stroke-width="2" fill="none"/></svg></span></span></div>
    </div>
  </div>
  <div class="form-title" style="top:462px">How Can We Help?</div>
  <div class="field focus" style="left:91px;top:515px;width:378px">First Name*</div>
  <div class="field" style="left:481px;top:515px;width:379px">Last Name*</div>
  <div class="field" style="left:91px;top:561px;width:378px">E-mail Adress*</div>
  <div class="field" style="left:481px;top:561px;width:379px">Services*<svg class="caret" width="14" height="8" viewBox="0 0 14 8"><path d="M0 0h14L7 8z" fill="#1a1f26"/></svg></div>
  <div class="field" style="left:91px;top:607px;width:769px;height:146px;line-height:20px;padding-top:8px">Massage*</div>
  <div class="map" style="top:767px" role="img" aria-label="Map showing the office location with a pin"></div>

  <div class="footer" style="top:1041px">© 2023 Copyright Korvane Consulting. All Right Reserved.</div>
  <div class="sidebar" style="height:1041px">
    <div class="menu-btn"><svg width="18" height="14" viewBox="0 0 18 14"><path d="M0 1h18M0 7h12M0 13h16" stroke="#fff" stroke-width="2"/></svg></div>
    <div class="side-label" style="top:150px">Contact Us</div>
    <div class="social outline" style="top:963px"></div>
    <div class="social filled" style="top:1009px"></div>
  </div>
  <div class="topbar">
    <div class="brand"><span class="brand-mark"></span>Korvane Consulting</div>
    <div class="nav">
      <div class="nav-item" style="left:542px;width:60px">Home</div>
      <div class="nav-item" style="left:630px;width:50px">About</div>
      <div class="nav-item" style="left:718px;width:64px">Services</div>
      <div class="nav-item active" style="left:816px;width:92px">Contact Us</div>
    </div>
    <div class="cta">Get Started<span class="arrow"><svg width="16" height="14" viewBox="0 0 16 14"><path d="M1 7h13M8 1l6 6-6 6" stroke="#fff" stroke-width="2" fill="none"/></svg></span></div>
  </div>
</section>

</body>
</html>
```